High Quality fast food restaurant - Tomanyo

Tomanyo is a fast food company with its target's focused on logistic, simplicity, high quality, freshness and modern.

We need a web design where the customers can get a complete idea of our high quality completeness, we want to take fast food to a new upper level.

We would like to see the colours of wood and metal. Pictures have been attached of our local.

We would like to have something in similar to: http://www.qpz.example/
Updates

Images for the food we are going to sell can be found here: http://shrt.example/uWQa7

It will be the images with rice, french fries or pita bread.

Target Market(s)

The fast food eating people between sloppy food and restaurant level.

Industry/Entity Type

Fast Food Restaurant

Requirements
Should not have
• No Flash or Java

```html
<!DOCTYPE html>
<html lang="en">
<head>
<meta charset="utf-8">
<title>Tomanyo – Can you handle the taste?</title>
<link href="https://fonts.googleapis.com/css2?family=Bebas+Neue&family=Signika:wght@400;600&display=swap" rel="stylesheet">
<style>
  :root {
    --wood-dark: #4a2c1a;
    --wood-mid: #8a5a36;
    --wood-light: #c79a6c;
    --hero-orange: #e5721a;
    --hero-deep: #b8410f;
    --nav-bg: rgba(48, 40, 38, 0.92);
    --nav-line: rgba(255, 255, 255, 0.12);
    --panel-bg: rgba(255, 255, 255, 0.94);
    --panel-foot: #3b3230;
    --ink: #2c2624;
    --ink-soft: #6d6360;
    --badge: #3f3532;
    --badge-text: #f4c95a;
    --white: #ffffff;
    --social-a: #3b6fb6;
    --social-b: #4fb6e6;
  }
  * { margin: 0; padding: 0; box-sizing: border-box; }
  html, body { width: 1200px; height: 1200px; overflow: hidden; }
  body {
    position: relative;
    font-family: "Signika", Arial, sans-serif;
    color: var(--ink);
    background: var(--wood-mid);
  }
  .wood-floor {
    position: absolute; inset: 0;
    background:
      radial-gradient(ellipse 45% 30% at 50% 92%, rgba(255,235,200,0.55), transparent 70%),
      linear-gradient(180deg, var(--wood-dark) 0%, var(--wood-mid) 45%, var(--wood-light) 85%, #b98a5c 100%);
  }
  .hero-photo {
    position: absolute; left: 22px; top: 0; width: 1156px; height: 502px;
    background:
      radial-gradient(ellipse 55% 60% at 50% 35%, #9c7a4a 0%, rgba(120,110,60,0.6) 45%, transparent 75%),
      linear-gradient(90deg, var(--hero-deep) 0%, var(--hero-orange) 50%, #f39a22 100%);
  }
  .main-nav {
    position: absolute; left: 186px; top: 12px; width: 828px; height: 69px;
    background: var(--nav-bg); border-radius: 5px;
    box-shadow: 0 3px 8px rgba(0,0,0,0.4);
    display: flex; align-items: center;
  }
  .main-nav ul { list-style: none; display: flex; height: 100%; }
  .main-nav li {
    display: flex; align-items: center; padding: 0 17px;
    border-right: 1px solid var(--nav-line);
    font-family: "Bebas Neue", Impact, sans-serif; font-size: 25px;
    color: var(--white); letter-spacing: 0.5px;
  }
  .social-links {
    margin-left: auto; height: 100%; display: flex; align-items: center; gap: 4px;
    padding: 0 18px 0 16px; border-left: 1px solid var(--nav-line);
  }
  .social-links span { width: 26px; height: 26px; border-radius: 3px; display: block; }
  .social-a { background: var(--social-a); }
  .social-b { background: var(--social-b); }
  .brand-name {
    position: absolute; left: 206px; top: 96px;
    font-family: "Bebas Neue", Impact, sans-serif; font-size: 58px;
    color: var(--white); letter-spacing: 1px;
  }
  .hero-headline {
    position: absolute; left: 572px; top: 94px;
    font-family: "Bebas Neue", Impact, sans-serif; font-weight: 400;
    font-size: 92px; line-height: 0.86; color: var(--white); letter-spacing: 1px;
  }
  .offer-sidebar {
    position: absolute; left: 189px; top: 378px; width: 253px; height: 428px;
    background: var(--panel-bg); border-radius: 4px;
    box-shadow: 0 4px 10px rgba(0,0,0,0.35); overflow: hidden;
  }
  .offer-item { position: absolute; left: 24px; width: 207px; }
  .offer-item:nth-child(1) { top: 24px; }
  .offer-item:nth-child(2) { top: 192px; }
  .offer-photo {
    width: 207px; height: 83px;
    background: linear-gradient(90deg, #d9d4cc 0%, #6b3a22 45%, #c7772c 75%, #7ea640 100%);
  }
  .offer-title-row { display: flex; align-items: center; gap: 14px; margin-top: 8px; }
  .offer-title {
    font-family: "Bebas Neue", Impact, sans-serif; font-size: 26px;
    font-weight: 400; line-height: 1; color: var(--ink);
  }
  .club-badge {
    background: var(--badge); color: var(--badge-text); border-radius: 3px;
    font-size: 11px; font-weight: 600; padding: 3px 9px;
  }
  .offer-desc { font-size: 10.5px; line-height: 14px; color: var(--ink); margin-top: 3px; }
  .sidebar-footer {
    position: absolute; left: 0; bottom: 0; width: 100%; height: 56px;
    background: var(--panel-foot); display: flex; align-items: center; justify-content: center;
    font-family: "Bebas Neue", Impact, sans-serif; font-size: 19px; color: var(--white);
  }
  .offers-panel {
    position: absolute; left: 462px; top: 378px; width: 549px; height: 428px;
    background: var(--panel-bg); border-radius: 4px;
    box-shadow: 0 4px 10px rgba(0,0,0,0.35);
  }
  .offers-heading {
    position: absolute; left: 35px; top: 22px;
    font-family: "Bebas Neue", Impact, sans-serif; font-weight: 400;
    font-size: 38px; color: var(--ink);
  }
  .offers-heading small { font-size: 24px; color: var(--ink-soft); }
  .feature-photo {
    position: absolute; left: 36px; top: 93px; width: 232px; height: 129px;
    background: linear-gradient(120deg, #3a2a20 0%, #c08a4e 40%, #d4462c 65%, #e9e4d8 100%);
  }
  .body-copy { font-size: 10.5px; line-height: 15px; color: var(--ink); }
  .copy-left { position: absolute; left: 36px; top: 228px; width: 232px; }
  .copy-right { position: absolute; left: 291px; top: 90px; width: 236px; }
  .panel-links {
    position: absolute; left: 321px; top: 282px; list-style: none;
    font-family: "Bebas Neue", Impact, sans-serif; font-size: 17px; line-height: 24px; color: var(--ink);
  }
</style>
</head>
<body>
  <div class="wood-floor" role="img" aria-label="Wooden plank floor and wall in warm brown tones with a soft spotlight"></div>
  <div class="hero-photo" role="img" aria-label="Close-up of a kebab sandwich with lettuce, tomato, cucumber and onion on an orange background"></div>

  <nav class="main-nav">
    <ul>
      <li>Start</li><li>Menu</li><li>Offers</li><li>Locations</li><li>About us</li><li>Contact</li>
    </ul>
    <div class="social-links"><span class="social-a"></span><span class="social-b"></span></div>
  </nav>

  <div class="brand-name">Tomanyo</div>
  <h1 class="hero-headline">Can you handle<br>the taste?</h1>

  <aside class="offer-sidebar">
    <div class="offer-item">
      <div class="offer-photo" role="img" aria-label="Kebab pita plate with grilled meat, vegetables and garlic yoghurt"></div>
      <div class="offer-title-row"><h3 class="offer-title">Kebab Pita</h3><span class="club-badge">Club-offer!</span></div>
      <p class="offer-desc">Grilled kebab with pitabread, salad and garlic yoghurt. Free drink (40cl) included.</p>
    </div>
    <div class="offer-item">
      <div class="offer-photo" role="img" aria-label="Kebab pita plate with grilled meat, vegetables and garlic yoghurt"></div>
      <div class="offer-title-row"><h3 class="offer-title">Kebab Pita</h3><span class="club-badge">Club-offer!</span></div>
      <p class="offer-desc">Grilled kebab with pitabread, salad and garlic yoghurt. Free drink (40cl) included.</p>
    </div>
    <div class="sidebar-footer">» Show me all your offers!</div>
  </aside>

  <section class="offers-panel">
    <h2 class="offers-heading">Hot offers! <small>From our kitchen</small></h2>
    <div class="feature-photo" role="img" aria-label="Wrapped pita sandwiches with fresh tomato salsa on a plate"></div>
    <p class="body-copy copy-left">Lorem ipsum dolor sit amet, consectetur adipisicing elit, sed do eiusmod tempor incididunt ut labore et dolore magna aliqua. Ut enim ad minim veniam, quis nostrud exercitation ullamco laboris nisi ut aliquip ex ea commodo consequat. Duis aute irure dolor in reprehenderit in voluptate.</p>
    <p class="body-copy copy-right">Lorem ipsum dolor sit amet, consectetur adipisicing elit, sed do eiusmod tempor incididunt ut labore et dolore magna aliqua. Ut enim ad minim veniam, quis nostrud exercitation ullamco laboris nisi ut aliquip ex ea commodo consequat. Duis aute irure dolor in reprehenderit in voluptate velit esse cillum dolore eu fugiat nulla pariatur. Excepteur sint occaecat cupidatat non proident, sunt in culpa qui officia deserunt mollit anim id est laborum.</p>
    <ul class="panel-links">
      <li>» Show me the menu already!</li>
      <li>» Get the Tomanyo-club card</li>
    </ul>
  </section>
</body>
</html>
```